The Web Promotion Playbook for Yard & Patio Construction Crews

We need a book cover design that is for a book targeting landscape and outdoor living contractors that helps them grow their business using online marketing.

We run a business focused on this industry so you can see what we do: https://yardcrewgrowthworks.com/

The title is: The Web Promotion Playbook for Yard & Patio Construction Crews

The author is: Trent Varnholm
Some drafts have been done however they're still looking basic and somewhat amateur, we're looking for something that will stand out.

Target Market(s)

Landscape, Hardscape and Outdoor Living Contractors and Business Owners

Industry/Entity Type

Online Marketing

Font styles to use
Serif
Sans Serif

Requirements
Must have
• The part of the title that should stand out the most is the text "Web Promotion Playbook".
Should not have
• The color red

```html
<!DOCTYPE html>
<html lang="en">
<head>
<meta charset="utf-8">
<title>The Web Promotion Playbook for Yard &amp; Patio Construction Crews</title>
<link rel="stylesheet" href="https://fonts.googleapis.com/css2?family=Anton&family=Oswald:wght@500;600&display=swap">
<style>
  :root {
    --stage: #222222;
    --cover-green: #006128;
    --title-yellow: #ffcc00;
    --paper-white: #ffffff;
    --sky: #c9d6e0;
    --wood: #8a6548;
    --lawn: #3f7a2c;
    --pool: #2f6f7d;
    --dusk: #6d6a58;
    --lamp: #d9a25a;
  }
  * { margin: 0; padding: 0; box-sizing: border-box; }
  html, body {
    width: 1200px; height: 1200px; overflow: hidden;
    background: var(--stage);
  }
  .book-cover {
    position: absolute; left: 215px; top: 23px;
    width: 770px; height: 1154px;
    background: var(--cover-green);
    overflow: hidden;
  }
  .hero-photo {
    position: absolute; left: 0; top: 0; width: 770px; height: 330px;
    background: linear-gradient(180deg, var(--sky) 0%, #8fa39a 28%, var(--lawn) 48%, var(--wood) 62%, var(--pool) 82%, #5b4636 100%);
  }
  .footer-photo {
    position: absolute; left: 0; top: 840px; width: 770px; height: 314px;
    background:
      radial-gradient(ellipse at 25% 45%, rgba(217,162,90,.75) 0%, rgba(217,162,90,0) 40%),
      linear-gradient(180deg, #7f8d7e 0%, #3d5a35 35%, var(--dusk) 60%, var(--pool) 85%, #1f5c62 100%);
  }
  .torn-edges { position: absolute; left: 0; top: 0; }
  .cover-type {
    position: absolute; left: 0; top: 0; width: 770px; height: 1154px;
  }
  .author {
    font-family: "Oswald", sans-serif; font-weight: 600;
    font-size: 30px; letter-spacing: 5px; fill: var(--paper-white);
  }
  .title-lead { font-family: "Anton", sans-serif; font-size: 84px; fill: var(--title-yellow); }
  .title-key { font-family: "Anton", sans-serif; font-size: 158px; fill: var(--paper-white); }
  .subtitle {
    font-family: "Oswald", sans-serif; font-weight: 500;
    font-size: 48px; fill: var(--title-yellow);
  }
  .publisher-mark {
    position: absolute; left: 300px; top: 1044px;
    display: flex; align-items: center; gap: 8px;
    font-family: "Oswald", sans-serif; font-weight: 600;
    font-size: 17px; letter-spacing: .5px; color: var(--paper-white);
  }
  .publisher-mark .mark-square {
    width: 14px; height: 14px; background: var(--paper-white);
  }
</style>
</head>
<body>
  <div class="book-cover">
    <div class="hero-photo" role="img" aria-label="Modern backyard with wooden pergola, deck, lounge seating and a rectangular pool beside a lawn"></div>
    <div class="footer-photo" role="img" aria-label="Evening patio with stone columns and warm lights, a curved pool and a rock waterfall"></div>

    <svg class="torn-edges" width="770" height="1154" viewBox="0 0 770 1154" aria-hidden="true">
      <path fill="#ffffff" d="M0 304 L18 296 L34 305 L52 293 L70 301 L88 290 L104 300 L126 292 L146 303 L166 291 L186 298 L206 289 L228 302 L250 292 L272 300 L292 288 L314 299 L336 291 L356 304 L378 293 L400 300 L420 289 L442 302 L464 292 L486 299 L506 288 L528 301 L550 292 L572 303 L594 291 L616 299 L638 289 L660 302 L682 292 L704 300 L726 290 L748 301 L770 293 L770 334 L750 342 L730 331 L708 343 L688 332 L666 340 L646 330 L624 341 L602 333 L580 344 L560 332 L538 340 L516 330 L494 343 L472 333 L452 341 L430 331 L408 342 L386 332 L364 340 L344 330 L322 344 L300 333 L280 341 L258 331 L236 342 L214 332 L192 340 L170 330 L150 343 L128 333 L106 340 L84 331 L62 343 L40 333 L20 340 L0 331 Z"/>
      <path fill="#ffffff" d="M0 836 L20 828 L40 838 L62 826 L84 835 L106 824 L128 834 L150 826 L170 837 L192 825 L214 833 L236 823 L258 836 L280 826 L300 834 L322 822 L344 835 L364 825 L386 836 L408 826 L430 834 L452 823 L472 836 L494 826 L516 833 L538 823 L560 835 L580 826 L602 837 L624 825 L646 833 L666 823 L688 836 L708 826 L730 834 L750 824 L770 834 L770 868 L748 876 L726 865 L704 877 L682 866 L660 874 L638 864 L616 876 L594 866 L572 878 L550 867 L528 875 L506 864 L486 877 L464 867 L442 874 L420 864 L400 876 L378 866 L356 874 L336 864 L314 878 L292 867 L272 874 L250 864 L228 876 L206 866 L186 874 L166 864 L146 877 L126 867 L104 874 L88 865 L70 877 L52 867 L34 874 L18 864 L0 872 Z"/>
    </svg>

    <svg class="cover-type" width="770" height="1154" viewBox="0 0 770 1154">
      <text class="author" x="385" y="388" text-anchor="middle">TRENT VARNHOLM</text>
      <text class="title-lead" x="385" y="512" text-anchor="middle" textLength="640" lengthAdjust="spacingAndGlyphs">THE WEB PROMOTION</text>
      <text class="title-key" x="385" y="675" text-anchor="middle" textLength="674" lengthAdjust="spacingAndGlyphs">PLAYBOOK</text>
      <text class="subtitle" x="385" y="748" text-anchor="middle" textLength="560" lengthAdjust="spacingAndGlyphs">FOR YARD &amp; PATIO</text>
      <text class="subtitle" x="385" y="804" text-anchor="middle" textLength="440" lengthAdjust="spacingAndGlyphs">CONSTRUCTION CREWS</text>
    </svg>

    <div class="publisher-mark">
      <span class="mark-square"></span>
      <span class="publisher-name">YARD CREW GROWTH WORKS</span>
    </div>
  </div>
</body>
</html>
```